Audio-Visual & Video Communications Business Requires a Cutting-edge Business Card Design

LinkVessel is a new Audio-Visual & Video Communications company in Cape Town, South Africa that is looking for a cutting-edge business card design. We sell these products to the Corporate, Education & Hospitality markets and will also host an Online Shop for companies and individuals to purchase our products online.

We are already using the following two colours in our logo and draft website. Please incorporate these colours into the design. Please note that our website is still in the design stage if you need to visit it. Green #a0ce4e & Dark Grey #333333.
Updates

Hi,

Please note that I have uploaded our logo in an .eps format.

Target Market(s)

Corporate Companies, Education Institutions & Hospitality Markets

Industry/Entity Type

Business

Requirements
Nice to have
• It would be great if you could incorporate the services that we offer.

1. Consultation & Design
2. Project Management
3. Supply & Installation
4. Onsite Support Personal
5. Online Shop

```html
<!DOCTYPE html>
<html lang="en">
<head>
<meta charset="utf-8">
<title>LinkVessel Business Card</title>
<link href="https://fonts.googleapis.com/css2?family=Open+Sans:wght@300;400;600;700&display=swap" rel="stylesheet">
<style>
  :root {
    --green: #a0ce4e;
    --green-deep: #8fbd42;
    --dark: #333333;
    --white: #ffffff;
    --backdrop: #e6e6e6;
    --shadow: rgba(0, 0, 0, 0.18);
  }
  * { box-sizing: border-box; margin: 0; padding: 0; }
  html, body {
    width: 1200px;
    height: 900px;
    overflow: hidden;
  }
  body {
    background: var(--backdrop);
    font-family: "Open Sans", Arial, sans-serif;
    display: flex;
    flex-direction: column;
    align-items: center;
    justify-content: center;
    gap: 56px;
  }
  .card {
    position: relative;
    width: 648px;
    height: 360px;
    overflow: hidden;
    box-shadow: 0 10px 28px var(--shadow);
  }

  /* Front */
  .card-front { background: var(--green); }
  .front-decor {
    position: absolute;
    left: -150px;
    top: 20px;
    width: 320px;
    height: 320px;
    border-radius: 50%;
    background: var(--green-deep);
    opacity: 0.7;
  }
  .front-brand {
    position: absolute;
    right: 48px;
    top: 118px;
    text-align: center;
    color: var(--white);
  }
  .front-brand .brand-row {
    display: flex;
    align-items: center;
    gap: 14px;
    justify-content: center;
  }
  .brand-dot {
    width: 34px;
    height: 34px;
    border-radius: 50%;
    background: var(--white);
  }
  .front-brand .brand-name {
    font-size: 46px;
    font-weight: 700;
    letter-spacing: -0.5px;
    line-height: 1;
  }
  .front-brand .tagline {
    margin-top: 12px;
    font-size: 12.5px;
    font-weight: 400;
    letter-spacing: 0.2px;
  }

  /* Back */
  .card-back { background: var(--dark); color: var(--green); }
  .holder { position: absolute; left: 44px; top: 34px; }
  .holder-name { font-size: 38px; font-weight: 300; line-height: 1.05; }
  .holder-title { font-size: 17px; font-weight: 300; margin-top: 2px; }
  .contact-list {
    position: absolute;
    left: 44px;
    top: 130px;
    list-style: none;
    font-size: 13px;
    font-weight: 400;
  }
  .contact-list li {
    display: flex;
    align-items: flex-start;
    gap: 12px;
    line-height: 1.35;
    margin-bottom: 7px;
  }
  .contact-list svg { width: 15px; height: 15px; flex: none; margin-top: 1px; fill: var(--green); }
  .back-brand {
    position: absolute;
    right: 40px;
    top: 230px;
    display: flex;
    align-items: center;
    gap: 12px;
  }
  .back-brand .brand-dot { background: var(--green); width: 28px; height: 28px; }
  .back-brand .brand-name { font-size: 36px; font-weight: 700; color: var(--green); line-height: 1; }
  .services {
    position: absolute;
    left: 0;
    right: 0;
    bottom: 12px;
    display: flex;
    justify-content: space-between;
    padding: 0 24px;
    list-style: none;
    font-size: 11.5px;
    font-weight: 400;
  }
  .service-band {
    position: absolute;
    left: 0;
    right: 0;
    bottom: 0;
    height: 7px;
    background: var(--green);
  }
</style>
</head>
<body>

  <section class="card card-front" aria-label="Business card front">
    <div class="front-decor"></div>
    <div class="front-brand">
      <div class="brand-row">
        <span class="brand-dot"></span>
        <span class="brand-name">LinkVessel</span>
      </div>
      <p class="tagline">Leaders in Audio-Visual &amp; Video Communications</p>
    </div>
  </section>

  <section class="card card-back" aria-label="Business card back">
    <div class="holder">
      <h1 class="holder-name">John Doe</h1>
      <p class="holder-title">Job Title</p>
    </div>

    <ul class="contact-list">
      <li>
        <svg viewBox="0 0 16 16" aria-hidden="true"><path d="M3.6 1.2l2.2 2.6-1.3 1.7c.9 2 2.4 3.5 4.4 4.4l1.7-1.3 2.6 2.2-1.4 2.6C7 13.2 2.8 9 1 3.2z"/></svg>
        <span>XXX XXX XXXX</span>
      </li>
      <li>
        <svg viewBox="0 0 16 16" aria-hidden="true"><path d="M1 3h14v10H1zM2.4 4.2L8 8.6l5.6-4.4z" fill-rule="evenodd"/></svg>
        <span>enquiries@linkvessel.com</span>
      </li>
      <li>
        <svg viewBox="0 0 16 16" aria-hidden="true"><path d="M8 1a7 7 0 100 14A7 7 0 008 1zm-.7 1.6v2.8H5.1c.5-1.4 1.3-2.5 2.2-2.8zm1.4 0c.9.3 1.7 1.4 2.2 2.8H8.7zM4.8 6.8h2.5v2.4H4.8zm3.9 0h2.5v2.4H8.7zM2.5 6.8h1c-.1.8-.1 1.6 0 2.4h-1a5.6 5.6 0 010-2.4zm10 0h1a5.6 5.6 0 010 2.4h-1c.1-.8.1-1.6 0-2.4zM5.1 10.6h2.2v2.8c-.9-.3-1.7-1.4-2.2-2.8zm3.6 0h2.2c-.5 1.4-1.3 2.5-2.2 2.8z"/></svg>
        <span>linkvessel.com</span>
      </li>
      <li>
        <svg viewBox="0 0 16 16" aria-hidden="true"><path d="M8 1a5 5 0 00-5 5c0 3.6 5 9 5 9s5-5.4 5-9a5 5 0 00-5-5zm0 7a2 2 0 110-4 2 2 0 010 4z"/></svg>
        <span>PO Box 2140, Kloofview, Cape Town<br>8001, South Africa</span>
      </li>
    </ul>

    <div class="back-brand">
      <span class="brand-dot"></span>
      <span class="brand-name">LinkVessel</span>
    </div>

    <ul class="services">
      <li>Consultation &amp; Design</li>
      <li>Project Management</li>
      <li>Supply &amp; Installation</li>
      <li>Onsite Support Personal</li>
      <li>Online Shop</li>
    </ul>
    <div class="service-band"></div>
  </section>

</body>
</html>
```